New LLC consulting company needs a business card design

I need a business card design for new company in Alexandria Virginia called TK Verdant Consulting LLC. The company is focused on consulting for defense and national security issues with expertise in nuclear and space topics. I would like to see designs that are simple and I am open to colors except for brown.

Target Market(s)

All businesses that are seeking consulting help

Industry/Entity Type

Consulting

Contact Information for Business Card

Name of company - TK Verdant Consulting LLC; name (Delia Hawke) President; email: hawkedr41@mailbox-example.net; Phone: 555-271-9043

Requirements
Must have
• The details described above
Nice to have
• I'm open to all ideas
Should not have
• No brown

```html
<!DOCTYPE html>
<html lang="en">
<head>
<meta charset="utf-8">
<title>TK Verdant Consulting LLC — Business Card</title>
<link href="https://fonts.googleapis.com/css2?family=Inter:wght@600&family=Montserrat:wght@400;600&display=swap" rel="stylesheet">
<style>
  :root {
    --backdrop: #949494;
    --navy: #07284c;
    --paper: #ffffff;
    --text-grey: #4a4a4a;
    --accent-red: #d3222a;
    --rule: #8a8a8a;
  }
  html, body {
    margin: 0;
    padding: 0;
    width: 1200px;
    height: 1200px;
    overflow: hidden;
    background: var(--backdrop);
  }
  .card {
    position: absolute;
    left: 179px;
    width: 862px;
    height: 496px;
    box-sizing: border-box;
  }
  .card--front {
    top: 85px;
    background: var(--navy);
    display: flex;
    align-items: center;
    justify-content: center;
  }
  .company-name {
    margin: 0 0 16px;
    font-family: "Inter", sans-serif;
    font-weight: 600;
    font-size: 42px;
    color: var(--paper);
    letter-spacing: 0.2px;
  }
  .card--back {
    top: 622px;
    background: var(--paper);
  }
  .details {
    position: absolute;
    left: 0;
    right: 0;
    top: 205px;
    display: flex;
    justify-content: center;
    align-items: flex-start;
  }
  .identity {
    text-align: right;
  }
  .person-name {
    margin: 0;
    font-family: "Montserrat", sans-serif;
    font-weight: 600;
    font-size: 38px;
    line-height: 1;
    color: var(--navy);
  }
  .person-title {
    margin: 12px 0 0;
    font-family: "Montserrat", sans-serif;
    font-weight: 400;
    font-size: 21px;
    color: var(--text-grey);
  }
  .divider {
    width: 1px;
    height: 66px;
    margin: 9px 18px 0;
    background: var(--rule);
    flex: none;
  }
  .contact-list {
    margin: 7px 0 0;
    padding: 0;
    list-style: none;
    font-family: "Montserrat", sans-serif;
    font-size: 21px;
    color: var(--text-grey);
  }
  .contact-item {
    display: flex;
    align-items: center;
    height: 37px;
    letter-spacing: 0.3px;
    white-space: nowrap;
  }
  .contact-icon {
    width: 24px;
    height: 24px;
    margin-right: 10px;
    flex: none;
  }
</style>
</head>
<body>
  <section class="card card--front">
    <h1 class="company-name">TK Verdant Consulting LLC</h1>
  </section>

  <section class="card card--back">
    <div class="details">
      <div class="identity">
        <p class="person-name">Delia Hawke</p>
        <p class="person-title">President</p>
      </div>
      <div class="divider"></div>
      <ul class="contact-list">
        <li class="contact-item">
          <svg class="contact-icon" viewBox="0 0 24 24" aria-hidden="true">
            <path fill="var(--accent-red)" d="M6.6 10.8a15.1 15.1 0 0 0 6.6 6.6l2.2-2.2c.3-.3.7-.4 1-.2 1.1.4 2.3.6 3.6.6.6 0 1 .4 1 1V20c0 .6-.4 1-1 1A17 17 0 0 1 3 4c0-.6.4-1 1-1h3.5c.6 0 1 .4 1 1 0 1.3.2 2.5.6 3.6.1.3 0 .7-.2 1z"/>
            <path fill="none" stroke="var(--accent-red)" stroke-width="1.8" stroke-linecap="round" d="M14 3.5a7 7 0 0 1 6.5 6.5M14 7a3.5 3.5 0 0 1 3 3"/>
          </svg>
          <span>555-271-9043</span>
        </li>
        <li class="contact-item">
          <svg class="contact-icon" viewBox="0 0 24 24" aria-hidden="true">
            <rect x="1" y="5" width="22" height="15" fill="var(--accent-red)"/>
            <path fill="none" stroke="#fff" stroke-width="1.4" d="M1.5 5.5 12 13.5 22.5 5.5M1.5 19.5l8-7M22.5 19.5l-8-7"/>
          </svg>
          <span>hawkedr41@mailbox-example.net</span>
        </li>
      </ul>
    </div>
  </section>
</body>
</html>
```